" ATENDEMOS OS CLIENTE E ANALISAMOS O PROBLEMA QUE NOS APRESENTA. PEDIMOS DOCUMENTAÇÃO PERTINENTE A CADA CASO E DOCUMENTAÇÃO COMPLEMENTAR. SE PRECISAR DE RETIFICAÇÃO , FAZEMOS REQUERIMENTO POR ESCRITO ÀS EMPRESAS NECESSÁRIAS. COM A DOCUMENTAÇÃO EM MÃOS AVALIAMOS E APRESENTAMOS AO CLIENTE AS SOLUÇOES CABÍVEIS, ORIENTANDO QUAL O MELHOR CAMINHO A TOMAR. "

```html
<!DOCTYPE html>
<html lang="pt-BR">
<head>
<meta charset="utf-8">
<title>Assinatura de e-mail — Ferraz &amp; Monteiro</title>
<link rel="stylesheet" href="https://fonts.googleapis.com/css2?family=Cinzel:wght@500&family=Arimo:wght@400&display=swap">
<style>
  :root {
    --page: #ffffff;
    --gold: #b8995a;
    --text: #8a8a8a;
  }
  * { margin: 0; padding: 0; box-sizing: border-box; }
  html, body {
    width: 1200px;
    height: 1200px;
    overflow: hidden;
    background: var(--page);
  }
  .canvas {
    width: 1200px;
    height: 1200px;
    display: flex;
    align-items: center;
    justify-content: center;
  }
  .signature {
    display: flex;
    align-items: center;
  }
  .brand {
    display: flex;
    align-items: center;
    gap: 22px;
    padding-right: 44px;
  }
  .brand-mark {
    width: 58px;
    height: 58px;
    background: var(--gold);
    flex: none;
  }
  .brand-name {
    font-family: "Cinzel", serif;
    font-weight: 500;
    font-size: 44px;
    line-height: 1.1;
    letter-spacing: 1px;
    color: var(--gold);
    text-transform: uppercase;
  }
  .divider {
    width: 3px;
    height: 200px;
    background: var(--gold);
    opacity: 0.7;
  }
  .contacts {
    list-style: none;
    padding-left: 36px;
    font-family: "Arimo", sans-serif;
    font-size: 24px;
    color: var(--text);
    line-height: 1.35;
  }
  .contact {
    display: flex;
    align-items: flex-start;
    gap: 16px;
    margin: 8px 0;
  }
  .contact-icon {
    width: 24px;
    height: 24px;
    flex: none;
    margin-top: 3px;
  }
</style>
</head>
<body>
<main class="canvas">
  <section class="signature">
    <div class="brand">
      <span class="brand-mark"></span>
      <span class="brand-name">Ferraz &amp;<br>Monteiro</span>
    </div>
    <div class="divider"></div>
    <ul class="contacts">
      <li class="contact">
        <svg class="contact-icon" viewBox="0 0 24 24" aria-hidden="true">
          <circle cx="12" cy="12" r="11" fill="none" stroke="#b8995a" stroke-width="1.6"/>
          <path d="M8.5 7c.6-.5 1.3-.4 1.6.2l.9 1.7c.3.5.1 1.1-.3 1.4l-.6.4c.6 1.4 1.6 2.4 3 3l.4-.6c.3-.4.9-.6 1.4-.3l1.7.9c.6.3.7 1 .2 1.6-1 1.1-2.4 1.3-3.8.6-2.2-1.1-3.9-2.8-5-5-.7-1.4-.5-2.8.5-3.9z" fill="#b8995a"/>
        </svg>
        <span>55 11 3047-6120</span>
      </li>
      <li class="contact">
        <svg class="contact-icon" viewBox="0 0 24 24" aria-hidden="true">
          <circle cx="12" cy="12" r="11" fill="none" stroke="#b8995a" stroke-width="1.6"/>
          <circle cx="12" cy="12" r="6" fill="none" stroke="#b8995a" stroke-width="1.4"/>
          <ellipse cx="12" cy="12" rx="2.6" ry="6" fill="none" stroke="#b8995a" stroke-width="1.2"/>
          <line x1="6" y1="12" x2="18" y2="12" stroke="#b8995a" stroke-width="1.2"/>
        </svg>
        <span>www.ferrazmonteiro.adv.br</span>
      </li>
      <li class="contact">
        <svg class="contact-icon" viewBox="0 0 24 24" aria-hidden="true">
          <circle cx="12" cy="12" r="11" fill="none" stroke="#b8995a" stroke-width="1.6"/>
          <path d="M12 5.5a4.2 4.2 0 0 0-4.2 4.2c0 3.1 4.2 8.3 4.2 8.3s4.2-5.2 4.2-8.3A4.2 4.2 0 0 0 12 5.5zm0 5.9a1.7 1.7 0 1 1 0-3.4 1.7 1.7 0 0 1 0 3.4z" fill="#b8995a"/>
        </svg>
        <span>Rua Alameda dos Ipês, 418, Vila Serena<br>São Paulo/SP - CEP: 04512-030</span>
      </li>
    </ul>
  </section>
</main>
</body>
</html>
```